依頼詳細
◇必須項目
・パララックス実装
・各メニューのアイコンなどでわかりやすくしてほしい
・英語の表記は出来る限り減らして欲しい
・今後観光のサイトを作成の予定があるのでバナーで飛べるようにしてほしい。
・現行の黒いサイトへのリンクも必要。

◇参考サイト
ミルヴェスタ  http://www.web-morvesta.net/ デザイン性があってブランド感が好き
ソビエント http://tovira.kumogi.ne.jp/client-check/sobient/index.html ロゴなどがああって分かりやすいから好き。

◇現行サイト
リニューアル予定サイトhttp://www.rensho-kyoto.co.jp/
サテライトサイトhttp://www.rensho-kyoto.com/

◇サイトマップ
①Home
② 8つのこだわり
③結婚指輪
④ 婚約指輪
⑤セット指輪
⑥ アクセサリー
⑦ デザイナー紹介
⑧店舗紹介
⑨お問い合わせ
⑩BLOG(一覧)
⑪BLOG(詳細)
⑫NEWS(一覧)
⑬NEWS(詳細)
⑭ご来店の前に
⑮結婚までの流れ
⑯お客様の声(一覧)
⑰お客様の声(詳細)
⑱HOW TO (ジュエリーの知識など)

◇優先事項
1.凝ったデザイン
2.ユーザビリティー
3.編集更新 ※詳しいので難しくても大丈夫

◇期待する効果
1.ブランディング
2.認知度の向上
3.SEO対策

◇ターゲット
【性別】女性
【年代】20代後半~40代
【属性】会社員 自営業

◇sns
shashingram 会社用 後々やる予定
kaobook 会社用
tsubuyaki 会社用

その他
予約システム
サイトURL
http://www.rensho-kyoto.co.jp/
ページ数
1ページ
希望イメージ
シンプル 複雑
単色 カラフル
暗い 明るい
日常 高級
遊び心 厳粛
未来的 伝統的
女性的 男性的
希望する色
カラーは基本的にお任せします。紫や濃い青色は縁起的に控えて下さい。
納品ファイル
• イラストレーター形式 (.ai)
• フォトショップ形式 (.psd)
• PNG形式 (.png)
補足説明
素材①
店内写真などをブリムコンテナを使って、アップしています。
下記URLよりダウンロードしてください。
■ダウンロードURL:
http://brimcontena.jp/download/9a1c3e7b2d4f6a8c0e1b3d5f7a9c2e4b6d8f0a1c
http://brimcontena.jp/download/7e2b4d6f8a0c1e3b5d7f9a2c4e6b8d0f1a3c5e7b

ダウンロードパスワード pass

素材②
ピクセノ:https://jp.pixeno-stock.com/
当社で定期契約をしています。クレジット購入のみのもの以外をご利用下さい。
また定期契約のものは弊社の負担となり、ランサー様に負担はありません。
カンプ画像を入れてください。

素材③
現行サイトより引用してください。
URL:http://www.rensho-kyoto.co.jp/
画像やテキストに関しては一旦引き抜いて頂いて構いません。

提案がないため、延長をさせて頂きます。
宜しくお願いたします!
もう少し提案が見たいため、延長を行わせて頂きます!
宜しくお願い致します!
提案が少ない為、延長させて頂きます。
テイストが少し違う部分もありますので詳細に関しては、別途報告させて頂きます。
宜しくお願い致します!
お世話になります。
テイストの伝え方が決定しましたのでお伝えします。

サイト全体の色味に関してですが、参考サイトをとして上げている、グレーやベージュなどを上手く使って和の雰囲気を出してほしいです。※全体的に緑を全面に打ち出したカラーが多いので少し変えてほしいです。
和に関しては、鳳林寺より雪峯寺、平安より室町、舞妓より芸子のイメージを考えています。パッと艶やかな京都ではなく京都の落ち着いた部分をメインに打ち出して頂きたいです。
また、和の雰囲気の出し方ですが画像に頼ったものはやめていただきたいです。
例えば、画像部分をグレーのダミー画像を使ったとしても和を感じれる様にデザインをお願いします。
全体的に画像に頼ったデザインが多いので画像を切ってはっただけのようなデザインは控えていただくようにお願いします。
ただ、和柄を使うだけではなく日本特有の間のとり方を使って平坦なデザインにならない様にお願いします。(和柄を使ってはだめなわけではありません。)
HPを見た人すべてが良いと感じるデザインでなくても問題ありませんがブランドのイメージをHP上で打ち出す表現は必須です。
何処かで見たことのあるデザインだけではなく、あまり見たことのないサイトデザインを希望しています。
自分自身デザイナーなのでデザインの意図や意味を大事にしています。
WEB上での動的な動きを含めて、和のテイストをより感じれるようなデザインが理想的です。
出来る限りデザインの意味や動的要因の説明を含めて提案を頂ければ幸いです。

ひと目見て気に入りました。

とてもデザイン性が高く満足しております。

```html
<!DOCTYPE html>
<html lang="ja">
<head>
<meta charset="utf-8">
<title>京都 蓮匠 | 結婚指輪・婚約指輪</title>
<link href="https://fonts.googleapis.com/css2?family=Noto+Serif+JP:wght@400;600&family=Noto+Sans+JP:wght@400&display=swap" rel="stylesheet">
<style>
:root{
  --ink:#3a3532;
  --muted:#8a827c;
  --line:#e3dcd6;
  --pink:#d88d98;
  --pink-soft:#e8aeb6;
  --olive:#8c9a2c;
  --olive-dark:#5f6b1a;
  --red:#9d2b2d;
  --grey:#cfcfcf;
  --paper:#ffffff;
  --foot:#eee2e3;
  --link:#4a7cc2;
}
*{margin:0;padding:0;box-sizing:border-box}
html,body{width:1200px;height:4956px;overflow:hidden;background:var(--paper)}
body{position:relative;font-family:"Noto Serif JP",serif;color:var(--ink)}
.block{position:absolute;left:0;width:1200px}
.ph{position:absolute}
a{color:inherit;text-decoration:none}

/* header */
.topline{top:8px;left:8px;font-size:11px;color:var(--muted);font-family:"Noto Sans JP",sans-serif;position:absolute}
.brand{position:absolute;top:22px;left:0;width:1200px;display:flex;flex-direction:column;align-items:center;gap:4px}
.brand-mark{width:48px;height:48px;border:2px solid var(--ink);border-radius:50%}
.brand-name{font-size:16px;letter-spacing:.4em;font-weight:600}
.cta{position:absolute;top:0;height:72px;width:176px;display:flex;align-items:center;justify-content:center;gap:8px;color:#fff;font-size:14px}
.cta.reserve{left:770px;background:var(--pink)}
.cta.contact{left:1000px;background:var(--ink)}
.nav{top:160px;height:48px;display:flex;justify-content:center;border-top:1px solid var(--line);border-bottom:1px solid var(--line)}
.nav a{width:180px;display:flex;align-items:center;justify-content:center;font-size:14px;border-right:1px solid var(--line)}
.nav a:first-child{border-left:1px solid var(--line)}

/* hero */
.hero{top:220px;height:440px;background:linear-gradient(100deg,#6f7d1c,#9aa83a 55%,#7d8a24)}
.hero-photo{left:0;top:0;width:760px;height:440px;background:radial-gradient(ellipse at 50% 55%,#e9ecef 0,#b9c0c4 22%,rgba(140,150,60,0) 48%),linear-gradient(180deg,rgba(0,0,0,0) 70%,rgba(80,50,20,.5))}
.hero-copy{position:absolute;right:60px;top:36px;display:flex;flex-direction:row-reverse;align-items:flex-start;gap:18px;color:#fff}
.hero-copy > *{writing-mode:vertical-rl}
.hero-copy .kyo{font-size:70px;font-weight:600;line-height:1}
.hero-copy p{font-size:22px;letter-spacing:.15em;line-height:1.2}
.hero-copy p.lead{margin-top:60px}

/* categories */
.cats{top:688px;height:152px;display:flex;justify-content:center;gap:8px}
.cat{width:250px;height:152px;position:relative;background:linear-gradient(180deg,#7d8a24 0 40px,#f1ece6 40px)}
.cat span{position:absolute;top:0;left:0;width:100%;height:40px;display:flex;align-items:center;justify-content:center;color:#fff;font-size:15px}
.cat i{position:absolute;left:40px;right:40px;top:60px;bottom:14px;background:radial-gradient(ellipse,#dfe2e5,#f1ece6 70%)}

/* headings */
.sec-title{position:absolute;left:0;width:1200px;text-align:center;font-size:22px;color:var(--pink);letter-spacing:.2em;font-weight:400}
.sec-title::after{content:"";display:block;width:120px;height:1px;background:var(--pink);margin:10px auto 0}
.about-mark{position:absolute;top:884px;left:575px;width:50px;height:50px;border:2px solid var(--ink);border-radius:50%;display:flex;align-items:center;justify-content:center;font-size:13px}
.about-text{position:absolute;top:1072px;left:250px;width:700px;text-align:center;font-size:13px;line-height:2.1;color:var(--muted)}

.list{position:absolute;left:300px;width:600px;list-style:none;font-size:12px;font-family:"Noto Sans JP",sans-serif}
.list li{display:flex;gap:30px;padding:10px 0;border-bottom:1px dotted var(--line)}
.list time{width:70px;flex:none;color:var(--muted)}
.list .link{color:var(--link)}
.more{position:absolute;left:510px;width:180px;height:32px;background:var(--pink);color:#fff;font-size:12px;display:flex;align-items:center;justify-content:center}

/* photo bands */
.band{height:248px}
/* features */
.feature{position:absolute;top:1832px;width:296px;text-align:center;font-size:15px;color:var(--pink)}
.feature i{display:block;margin-top:14px;height:256px}
/* banners */
.wide-banner{position:absolute;top:2160px;height:168px;width:512px;display:flex;align-items:flex-end;justify-content:flex-end;padding:20px 30px;font-size:28px;color:#fff;letter-spacing:.1em;white-space:nowrap}

/* voice */
.voice-box{position:absolute;top:3008px;left:88px;width:264px;height:280px;background:var(--pink-soft);color:#fff;display:flex;flex-direction:column;align-items:center;justify-content:center;gap:30px}
.voice-box h3{writing-mode:vertical-rl;font-size:26px;font-weight:400;letter-spacing:.3em}
.voice-box a{border:1px solid #fff;padding:6px 16px;font-size:12px}
.voice-list{position:absolute;top:3008px;left:370px;width:740px;list-style:none}
.voice-list li{display:flex;gap:20px;height:93px;border-bottom:1px dotted var(--line);padding:6px 0}
.voice-list i{width:80px;height:80px;flex:none;background:linear-gradient(135deg,#e7c9b4,#c89a7f)}
.voice-list div{font-size:12px;line-height:1.8;font-family:"Noto Sans JP",sans-serif}
.voice-list b{font-weight:400;color:var(--ink)}
.voice-list p{color:var(--muted)}

.howto{top:3360px;height:152px;left:88px;width:1024px;background:linear-gradient(90deg,var(--olive-dark),var(--olive) 60%,#7d8a24)}
.howto h2{position:absolute;left:30px;top:28px;color:#fff;font-size:48px;font-weight:600;letter-spacing:.05em}
.howto p{position:absolute;left:34px;top:96px;color:#fff;font-size:14px}

.sns{position:absolute;top:3584px;width:296px;height:356px;background:var(--grey);display:flex;align-items:center;justify-content:center;font-size:16px;font-family:"Noto Sans JP",sans-serif;color:#555}

.tour{position:absolute;top:4020px;left:88px;width:1024px;height:180px;display:flex}
.tour-red{width:460px;background:var(--red);color:#fff;display:flex;flex-direction:column;justify-content:center;padding-left:40px;gap:10px}
.tour-red strong{font-size:34px;font-weight:400;letter-spacing:.1em}
.tour-red span{font-size:14px}
.mens{position:absolute;top:4240px;left:88px;width:1024px;height:172px;background:#111;color:#fff;display:flex;align-items:center;justify-content:center;font-size:20px;letter-spacing:.2em}
.foot{top:4480px;height:476px;background:var(--foot)}
</style>
</head>
<body>

<header>
  <p class="topline">京都の結婚指輪・婚約指輪 蓮匠 手仕事で仕立てる二人だけの特別な一本</p>
  <div class="brand"><span class="brand-mark"></span><span class="brand-name">蓮匠</span></div>
  <a class="cta reserve" href="#">
    <svg width="16" height="16" viewBox="0 0 16 16"><rect x="1" y="3" width="14" height="12" fill="none" stroke="#fff"/><line x1="1" y1="7" x2="15" y2="7" stroke="#fff"/></svg>ご来店の予約</a>
  <a class="cta contact" href="#">
    <svg width="16" height="16" viewBox="0 0 16 16"><rect x="1" y="3" width="14" height="10" fill="none" stroke="#fff"/><polyline points="1,3 8,9 15,3" fill="none" stroke="#fff"/></svg>お問い合わせ</a>
  <nav class="block nav">
    <a href="#">トップページ</a><a href="#">商品一覧</a><a href="#">8つのこだわり</a><a href="#">デザイナー紹介</a><a href="#">BLOG</a><a href="#">店舗紹介</a>
  </nav>
</header>

<section class="block hero">
  <div class="ph hero-photo" role="img" aria-label="木の台に置かれた三本の結婚指輪と婚約指輪"></div>
  <div class="hero-copy"><span class="kyo">京</span><p>和の感性で</p><p class="lead">洗練された結婚指輪・婚約指輪</p></div>
</section>

<section class="block cats">
  <a class="cat" href="#"><span>結婚指輪</span><i role="img" aria-label="結婚指輪の写真"></i></a>
  <a class="cat" href="#"><span>婚約指輪</span><i role="img" aria-label="婚約指輪の写真"></i></a>
  <a class="cat" href="#"><span>セット指輪</span><i role="img" aria-label="セット指輪の写真"></i></a>
  <a class="cat" href="#"><span>アクセサリー</span><i role="img" aria-label="ネックレスの写真"></i></a>
</section>

<section>
  <div class="about-mark">蓮匠</div>
  <h2 class="sec-title" style="top:984px">蓮匠について</h2>
  <p class="about-text">京都で結婚指輪と婚約指輪を手がける工房として、職人の技と和の感性を一本に込めています。<br>お二人の想いを丁寧に伺い、日常に寄り添う美しい指輪をお仕立てします。<br>落ち着いた京都の空気の中で、ゆっくりとお選びいただける店づくりを大切にしています。</p>

  <h2 class="sec-title" style="top:1220px">ニュース</h2>
  <ul class="list" style="top:1272px">
    <li><time>2017.8.11</time><span>ここにニュースの内容が入ります。<span class="link">リンク付きの文字が入ります。</span></span></li>
    <li><time>2017.8.05</time><span>ここにニュースの内容が入ります。</span></li>
    <li><time>2017.7.21</time><span>ここにニュースの内容が入ります。新着情報が入ります。<br>ここにニュースの内容が入ります。新着情報が入ります。</span></li>
  </ul>
  <a class="more" href="#" style="top:1424px">ニュースを見る</a>
</section>

<div class="block band" style="top:1512px;background:linear-gradient(180deg,#3a2414,#b7854a 40%,#d8b07a 60%,#6a4424)" role="img" aria-label="木の棚に並ぶ指輪の写真"></div>

<section>
  <div class="feature" style="left:88px">8つのこだわり<i role="img" aria-label="木の指輪ケースが並ぶ写真" style="background:linear-gradient(135deg,#c9a77c,#8b6540)"></i></div>
  <div class="feature" style="left:452px">デザイナー紹介<i role="img" aria-label="デザイナーの集合写真" style="background:linear-gradient(135deg,#b8b0a8,#5b534c)"></i></div>
  <div class="feature" style="left:816px">店舗紹介<i role="img" aria-label="店内の写真" style="background:linear-gradient(135deg,#6a4c34,#c9a070)"></i></div>
</section>

<a class="wide-banner" href="#" style="left:88px;background:linear-gradient(90deg,#8a4a3c,#c0a0a0)" role="img" aria-label="着物姿の女性の写真と結婚までの流れ">結婚までの流れ</a>
<a class="wide-banner" href="#" style="left:600px;background:linear-gradient(90deg,#6e5a4a,#d7a4ab)" role="img" aria-label="店内の写真とご来店の前に">ご来店の前に</a>

<section>
  <h2 class="sec-title" style="top:2380px">ブログ</h2>
  <ul class="list" style="top:2432px">
    <li><time>2017.8.11</time><span>ここにブログの内容が入ります。<span class="link">リンク付きの文字が入ります。</span></span></li>
    <li><time>2017.8.05</time><span>ここにブログの内容が入ります。</span></li>
    <li><time>2017.7.21</time><span>ここにブログの内容が入ります。新着記事が入ります。<br>ここにブログの内容が入ります。新着記事が入ります。</span></li>
  </ul>
  <a class="more" href="#" style="top:2592px">ブログをもっと読む</a>
</section>

<div class="block band" style="top:2736px;height:192px;background:linear-gradient(90deg,#3a2a1c,#6e8a3a 20%,#b7c28a 40%,#5e4a30 60%,#8a7a6a 80%,#3a2a1c)" role="img" aria-label="京都の町並みの写真"></div>

<section>
  <div class="voice-box"><h3>お客様の声</h3><a href="#">お客様の声を見る</a></div>
  <ul class="voice-list">
    <li><i role="img" aria-label="お客様の写真"></i><div><b>2017.2.20　京都府 T様ご夫婦</b><p>丁寧な説明で安心して選ぶことができました。二人だけの指輪を大切にします。<br>ここにお客様の声が入ります。</p></div></li>
    <li><i role="img" aria-label="お客様の写真"></i><div><b>2017.2.20　大阪府 K様ご夫婦</b><p>丁寧な説明で安心して選ぶことができました。二人だけの指輪を大切にします。<br>ここにお客様の声が入ります。</p></div></li>
    <li><i role="img" aria-label="お客様の写真"></i><div><b>2017.2.20　滋賀県 S様ご夫婦</b><p>丁寧な説明で安心して選ぶことができました。二人だけの指輪を大切にします。<br>ここにお客様の声が入ります。</p></div></li>
  </ul>
</section>

<a class="block howto" href="#"><h2>HOW TO</h2><p>アクセサリーの知識と扱い方</p>
  <span class="ph" role="img" aria-label="指輪の写真" style="left:380px;top:0;width:400px;height:152px;background:radial-gradient(ellipse,#eef0f2,rgba(140,150,60,0) 60%)"></span></a>

<a class="sns" href="#" style="left:88px">tsubuyaki</a>
<a class="sns" href="#" style="left:452px">kaobook</a>
<a class="sns" href="#" style="left:816px">shashingram</a>

<a class="tour" href="#">
  <div class="tour-red"><strong>おいでやす、京都</strong><span>京都観光案内サイト</span></div>
  <div role="img" aria-label="京都の寺院と竹林の写真" style="flex:1;background:linear-gradient(90deg,#c98a9a,#4e6a3a 35%,#7a9a5a 55%,#a03a2a 75%,#4a6aa0)"></div>
</a>

<a class="mens" href="#">
  <span class="ph" role="img" aria-label="指輪の写真" style="left:40px;top:26px;width:200px;height:120px;background:radial-gradient(ellipse,#9aa83a,#111 70%)"></span>
  京都 蓮匠のメンズサイト
  <span class="ph" role="img" aria-label="指輪の写真" style="right:40px;top:26px;width:200px;height:120px;background:radial-gradient(ellipse,#9aa83a,#111 70%)"></span>
</a>

<footer class="block foot"></footer>
</body>
</html>
```